Wellness Wordpress Blog Redesign

I am looking to redesign by wordpress blog - www.MarenCrowleyActive.com. I would like to have a more personalized feel that resonates with my brand of Renewed Balance through fitness, nutrition, self care and self love. I'd like capabilities to do the following:

Ideally, I'd like to have the home page feature not only my latest blog posts or videos, but to also include a place to click to learn more about other facets of my business.

Ideally, I'd love to have a page layout of:

Home - main page to host key features of the brand & latest blog posts
About - Place to learn more about me and my brand
Blog -
Fitness - Host some videos and fitness tips and links to resources
Nutrition - Host some videos and recipes and links to resources
Self Care - Host some videos and self care tips and links to resources
Shop - Host a video (that can be changed of the product of the month) and links to other resources

Number of Pages Required

5+ page

Font styles to use
Serif
Decorative

Colors
85acd3
0393ce
00a990
6b449b
a64599
b8a6cd

Requirements
Must have
• Home - main page to host key features of the brand & latest blog posts
• About - Place to learn more about me and my brand
• Blog -
• Fitness - Host some videos and fitness tips and links to resources
• Nutrition - Host some videos and recipes and links to resources
• Self Care - Host some videos and self care tips and links to resources
• Shop - Host a video (that can be changed of the product of the month) and links to other resources
• Video / Mutlimedia capabilities
Nice to have
• Option to have a calendar of events widgets for people to sign up for events that I'm hosting

```html
<!DOCTYPE html>
<html lang="en">
<head>
<meta charset="utf-8">
<title>Maren Crowley – Training &amp; Coaching</title>
<link href="https://fonts.googleapis.com/css2?family=Mulish:wght@400;600;700;800&display=swap" rel="stylesheet">
<style>
:root{
  --purple:#6b449b;
  --teal:#00a990;
  --blue:#0393ce;
  --magenta:#a64599;
  --sky:#7198cb;
  --navy-blue:#1677c1;
  --light:#f2f2f2;
  --ink:#333;
  --muted:#666;
  --footer:#1c1f26;
}
*{box-sizing:border-box;margin:0;padding:0}
html,body{width:1200px;height:3689px;overflow:hidden}
body{font-family:'Mulish',sans-serif;color:var(--ink);background:#fff;position:relative}
section,header,footer{position:absolute;left:0;width:1200px}
h2.section-title{font-size:34px;font-weight:700;color:var(--purple);text-align:center;position:absolute;left:0;width:100%}

/* header */
.site-header{top:0;height:106px;background:#fff}
.brand{position:absolute;left:135px;top:26px;display:flex;align-items:center;gap:12px}
.brand-dot{width:14px;height:14px;border-radius:50%;background:var(--purple)}
.brand-name{font-size:30px;font-weight:800;color:var(--purple);line-height:1}
.brand-sub{position:absolute;left:161px;top:62px;font-size:9px;letter-spacing:3px;font-weight:800;color:var(--purple)}
.search{position:absolute;left:863px;top:25px;width:204px;height:29px;border:1px solid #ccc;font-size:11px;padding:7px 10px;color:#555}
.search svg{position:absolute;right:8px;top:8px}
.main-nav{position:absolute;right:133px;top:66px;display:flex;gap:28px;font-size:14px;color:#444}
.main-nav .active{color:var(--purple);font-weight:700}

/* hero */
.hero{top:106px;height:509px}
.hero-photo{position:absolute;inset:0;background:linear-gradient(90deg,#c9634a 0%,#e9dcd0 22%,#f5f2ee 40%,#f5f2ee 62%,#e6d8c8 80%,#c7573e 100%)}
.hero-arrow{position:absolute;top:240px;width:22px;height:22px;background:#333;color:#fff;font-size:12px;text-align:center;line-height:22px}
.hero-copy{position:absolute;left:0;width:100%;top:128px;text-align:center;font-size:32px;font-weight:800;line-height:43px;color:#444}
.t-teal{color:var(--teal)}.t-mag{color:var(--magenta)}.t-blue{color:var(--blue)}.t-purple{color:var(--purple)}
.hero-rule{position:absolute;left:430px;width:340px;top:276px;border-top:1px solid #999}
.hero-sub{position:absolute;left:0;width:100%;top:293px;text-align:center;color:#a0292d;font-size:16px;font-weight:600}
.email-field{position:absolute;width:340px;height:42px;background:#fff;border-radius:3px;font-size:13px;color:#555;padding:12px 20px}
.email-field svg{position:absolute;right:14px;top:14px}

/* welcome */
.welcome{top:615px;height:290px}
.welcome p{position:absolute;left:135px;width:932px;top:118px;font-size:13.5px;line-height:20px;color:#555;text-align:justify;text-align-last:center}

/* services */
.services{top:905px;height:435px;background:var(--light)}
.service-card{position:absolute;top:138px;width:295px;height:216px;border:2px solid var(--teal);text-align:center}
.service-icon{display:block;margin:22px auto 0}
.service-card h3{font-size:25px;font-weight:600;color:var(--teal);margin-top:18px}
.service-card p{font-size:10.5px;line-height:14px;color:#555;width:230px;margin:8px auto 0}

/* blog */
.blog{top:1340px;height:1119px;background:var(--sky)}
.blog .section-title{color:#fff}
.post{position:absolute;width:455px;height:410px;background:#f2f2f2}
.post-img{height:270px;position:relative}
.post-date{position:absolute;left:0;bottom:0;background:var(--teal);color:#fff;font-size:11px;padding:5px 14px}
.post h3{font-size:16px;font-weight:700;color:#222;margin:20px 18px 8px}
.post p{font-size:10.5px;line-height:16px;color:#555;margin:0 18px}
.post p a{color:var(--purple);font-weight:600;text-decoration:none}
.btn-outline{position:absolute;left:551px;top:1021px;width:98px;height:37px;background:#fff;color:var(--sky);font-size:15px;text-align:center;line-height:37px;border-radius:3px}

/* shop */
.shop{top:2459px;height:425px}
.product{position:absolute;top:130px;width:219px;height:219px;border:1px solid #e6e6e6;text-align:center;background:#fff}
.product-img{height:142px}
.product h4{font-size:13px;font-weight:400;color:#333;margin-top:18px}
.product span{display:block;font-size:13px;color:var(--blue);margin-top:4px}
.carousel-arrow{position:absolute;width:20px;height:30px}

/* events */
.events{top:2884px;height:369px;background:var(--light)}
.event{position:absolute;top:141px;width:213px;height:147px;background:#fff;padding:16px 18px}
.event time{font-size:13px;color:var(--blue);display:block}
.event p{font-size:10.5px;line-height:14px;color:#555;margin-top:10px}
.event a{display:block;margin-top:10px;font-size:10px;color:var(--blue);text-decoration:underline}

/* newsletter */
.newsletter{top:3253px;height:281px;background:var(--navy-blue);color:#fff}
.newsletter h2{position:absolute;width:100%;top:75px;font-size:30px;font-weight:700;text-align:center}
.newsletter p{position:absolute;width:100%;top:122px;font-size:17px;text-align:center}

/* footer */
.site-footer{top:3534px;height:155px;background:var(--footer);color:#aaa}
.social{position:absolute;left:0;width:100%;top:34px;display:flex;justify-content:center;gap:22px}
.social span{width:16px;height:16px;border-radius:50%;background:#9a9da3}
.footer-nav{position:absolute;width:100%;top:76px;text-align:center;font-size:11px;color:#bbb;word-spacing:4px}
.copyright{position:absolute;width:100%;top:102px;text-align:center;font-size:10px;color:#888}
</style>
</head>
<body>

<header class="site-header">
  <div class="brand"><span class="brand-dot"></span><span class="brand-name">Maren Crowley</span></div>
  <div class="brand-sub">TRAINING &amp; COACHING</div>
  <div class="search">Search
    <svg width="13" height="13" viewBox="0 0 13 13"><circle cx="5.5" cy="5.5" r="4" fill="none" stroke="#444" stroke-width="1.6"/><line x1="8.5" y1="8.5" x2="12" y2="12" stroke="#444" stroke-width="1.8"/></svg>
  </div>
  <nav class="main-nav"><span class="active">Home</span><span>About</span><span>Blog</span><span>Fitness</span><span>Nutrition</span><span>Selfcare</span><span>Shop</span><span>Contact us</span></nav>
</header>

<section class="hero">
  <div class="hero-photo" role="img" aria-label="Fresh vegetables, herbs and oil spoons arranged on a white tabletop"></div>
  <div class="hero-arrow" style="left:0">&#9664;</div>
  <div class="hero-arrow" style="right:0">&#9654;</div>
  <div class="hero-copy">
    Sharing My Passion for<br>
    <span class="t-teal">Health</span>, <span class="t-mag">Fitness</span> &amp; <span class="t-blue">Self Care</span><br>
    <span class="t-purple">to Help You Live Your Best Life</span>
  </div>
  <div class="hero-rule"></div>
  <div class="hero-sub">Subscribe for Newsletter</div>
  <div class="email-field" style="left:430px;top:334px">Email Address
    <svg width="16" height="12" viewBox="0 0 16 12"><rect width="16" height="12" fill="#6b449b"/><path d="M0 0 L8 7 L16 0" fill="none" stroke="#fff" stroke-width="1.4"/></svg>
  </div>
</section>

<section class="welcome">
  <h2 class="section-title" style="top:72px">Welcome to Maren Crowley</h2>
  <p>Fusce sollicitudin lorem et luctus volutpat. Proin placerat dapibus gravida. In tristique tristique nulla eget hendrerit. Maecenas vel tortor accumsan quam varius imperdiet vel eget elit. Aenean facilisis tincidunt lectus, id dictum nisi luctus eget. Vivamus efficitur ex condimentum, malesuada eros eget, feugiat nibh. Sed tellus ex, imperdiet eget gravida sit amet, volutpat eget turpis. In nec ultricies est. Etiam mattis augue vehicula odio posuere, sit amet tempus lectus luctus. Nulla facilisi. Etiam vel massa elementum, bibendum tellus venenatis, feugiat massa.</p>
</section>

<section class="services">
  <h2 class="section-title" style="top:72px">Services</h2>
  <div class="service-card" style="left:133px">
    <svg class="service-icon" width="80" height="80" viewBox="0 0 80 80" aria-label="Dumbbell icon" role="img">
      <g fill="none" stroke="#00a990" stroke-width="2.4" stroke-linejoin="round" transform="rotate(-40 40 40)">
        <rect x="10" y="26" width="9" height="28" rx="2"/><rect x="19" y="31" width="7" height="18" rx="2"/>
        <rect x="61" y="26" width="9" height="28" rx="2"/><rect x="54" y="31" width="7" height="18" rx="2"/>
        <line x1="26" y1="40" x2="54" y2="40"/>
      </g>
    </svg>
    <h3>Fitness</h3>
    <p>Aliquam erat volutpat. Quisque aliquet ex nec est vestibulum pulvinar. Pellentesque convallis molestie enim sit amet.</p>
  </div>
  <div class="service-card" style="left:453px">
    <svg class="service-icon" width="80" height="80" viewBox="0 0 80 80" aria-label="Blender jar with heart icon" role="img">
      <g fill="none" stroke="#00a990" stroke-width="2.4" stroke-linejoin="round">
        <rect x="22" y="14" width="26" height="8" rx="2"/>
        <path d="M20 22 H50 L46 58 H24 Z"/>
        <rect x="20" y="58" width="30" height="12" rx="2"/>
        <line x1="24" y1="34" x2="46" y2="34"/>
        <path d="M62 24 C62 18 54 17 54 23 C54 17 46 18 46 24 C46 30 54 34 54 36 C54 34 62 30 62 24 Z" transform="translate(6 -6)"/>
      </g>
    </svg>
    <h3>Nutrition</h3>
    <p>Aliquam erat volutpat. Quisque aliquet ex nec est vestibulum pulvinar. Pellentesque convallis molestie enim sit amet.</p>
  </div>
  <div class="service-card" style="left:772px">
    <svg class="service-icon" width="80" height="80" viewBox="0 0 80 80" aria-label="Heart in circle self care icon" role="img">
      <g fill="none" stroke="#00a990" stroke-width="2.4" stroke-linejoin="round">
        <circle cx="40" cy="40" r="28"/>
        <path d="M40 54 C30 46 26 41 26 35 C26 29 34 26 40 33 C46 26 54 29 54 35 C54 41 50 46 40 54 Z"/>
      </g>
    </svg>
    <h3>Selfcare</h3>
    <p>Aliquam erat volutpat. Quisque aliquet ex nec est vestibulum pulvinar. Pellentesque convallis molestie enim sit amet.</p>
  </div>
</section>

<section class="blog">
  <h2 class="section-title" style="top:54px">Blog</h2>
  <article class="post" style="left:133px;top:126px">
    <div class="post-img" role="img" aria-label="Hands chopping vegetables on a wooden board" style="background:linear-gradient(160deg,#7a5a44,#9c7b5c 55%,#5d6e44)"><span class="post-date">January 12, 2018</span></div>
    <h3>3 Tips to Eat Clean This Year</h3>
    <p>Did you make a New Year's resolution to eat cleaner or lose weight? If so, you are in good company, since millions of people search online each January for how to get healthier in the new year. It's pretty clear that most people know… <a>Continue reading</a></p>
  </article>
  <article class="post" style="left:612px;top:126px">
    <div class="post-img" role="img" aria-label="Runner in motion past a white brick wall" style="background:linear-gradient(180deg,#eeeeee,#dedede 70%,#bdbdbd)"><span class="post-date">January 12, 2018</span></div>
    <h3>4 Post Marathon Recovery Tips</h3>
    <p>Race season is upon us and this weekend I was in town to support my friends and clients who ran the Lakeshore Marathon. I took part in a short race too and had a great time. I wanted to share tips for those new to running… <a>Continue reading</a></p>
  </article>
  <article class="post" style="left:133px;top:561px">
    <div class="post-img" role="img" aria-label="Colourful pH spectrum chart from acidic to alkaline foods" style="background:linear-gradient(90deg,#e86a5f,#f2a65a,#efd36a,#7cbf7c,#6fa4dc,#8a70c0)"><span class="post-date">January 12, 2018</span></div>
    <h3>Are you too Acidic? Try increasing your Alkalinity!</h3>
    <p>Are you too acidic? The typical modern diet is heavy, and it might be putting you at risk for having an overly acidic ecosystem in your body. Most people are eating foods that are highly processed and refined, packed with sugar. On top of that, we live in a society… <a>Continue reading</a></p>
  </article>
  <article class="post" style="left:612px;top:561px">
    <div class="post-img" role="img" aria-label="Sliced apple with a bowl of nut butter" style="background:linear-gradient(160deg,#f1ece5,#e6cba4 55%,#c9745e)"><span class="post-date">January 12, 2018</span></div>
    <h3>Plant Based Pre &amp; Post Workout Snacks</h3>
    <p>Recently, I've had a few clients who have a plant based diet and they have asked me for ideas of what to eat before and after their workouts. Many people get confused on what to eat, so I wanted to share some favorite options… <a>Continue reading</a></p>
  </article>
  <div class="btn-outline">View All</div>
</section>

<section class="shop">
  <h2 class="section-title" style="top:72px">Shop</h2>
  <svg class="carousel-arrow" style="left:58px;top:226px" viewBox="0 0 20 30"><path d="M15 3 L5 15 L15 27" fill="none" stroke="#999" stroke-width="2"/></svg>
  <svg class="carousel-arrow" style="left:1122px;top:226px" viewBox="0 0 20 30"><path d="M5 3 L15 15 L5 27" fill="none" stroke="#999" stroke-width="2"/></svg>
  <div class="product" style="left:133px"><div class="product-img" role="img" aria-label="Fruit, bread and cheese arrangement" style="background:linear-gradient(180deg,#f6f6f6,#eadcc2 60%,#d9a88a)"></div><h4>Vivamus efficitur</h4><span>$15.00</span></div>
  <div class="product" style="left:371px"><div class="product-img" role="img" aria-label="Blue sports water bottle" style="background:linear-gradient(90deg,#f6f6f6 30%,#bcdcf0 50%,#f6f6f6 70%)"></div><h4>Sed tellus ex</h4><span>$12.00</span></div>
  <div class="product" style="left:610px"><div class="product-img" role="img" aria-label="Rolled pink yoga mat" style="background:linear-gradient(180deg,#f6f6f6 25%,#f3c3da 50%,#f6f6f6 75%)"></div><h4>Etiam mattis</h4><span>$10.00</span></div>
  <div class="product" style="left:848px"><div class="product-img" role="img" aria-label="Pair of pink running shoes" style="background:linear-gradient(180deg,#f6f6f6 20%,#efb4cf 55%,#f6f6f6 85%)"></div><h4>Nulla facilisi</h4><span>$18.00</span></div>
</section>

<section class="events">
  <h2 class="section-title" style="top:76px">Events</h2>
  <svg class="carousel-arrow" style="left:58px;top:199px" viewBox="0 0 20 30"><path d="M15 3 L5 15 L15 27" fill="none" stroke="#999" stroke-width="2"/></svg>
  <svg class="carousel-arrow" style="left:1122px;top:199px" viewBox="0 0 20 30"><path d="M5 3 L15 15 L5 27" fill="none" stroke="#999" stroke-width="2"/></svg>
  <div class="event" style="left:133px"><time>7 July, 2018</time><p>Vivamus luctus justo, ultrices nec erat in, euismod iaculis mauris. Vivamus eleifend vitae nulla.</p><a>Read More</a></div>
  <div class="event" style="left:371px"><time>7 July, 2018</time><p>Vivamus luctus justo, ultrices nec erat in, euismod iaculis mauris. Vivamus eleifend vitae nulla.</p><a>Read More</a></div>
  <div class="event" style="left:610px"><time>7 July, 2018</time><p>Vivamus luctus justo, ultrices nec erat in, euismod iaculis mauris. Vivamus eleifend vitae nulla.</p><a>Read More</a></div>
  <div class="event" style="left:848px"><time>7 July, 2018</time><p>Vivamus luctus justo, ultrices nec erat in, euismod iaculis mauris. Vivamus eleifend vitae nulla.</p><a>Read More</a></div>
</section>

<section class="newsletter">
  <h2>Newsletter Signup</h2>
  <p>Phasellus nisl est, condimentum vitae faucibus in, sollicitudin</p>
  <div class="email-field" style="left:430px;top:158px">Email Address
    <svg width="16" height="12" viewBox="0 0 16 12"><rect width="16" height="12" fill="#6b449b"/><path d="M0 0 L8 7 L16 0" fill="none" stroke="#fff" stroke-width="1.4"/></svg>
  </div>
</section>

<footer class="site-footer">
  <div class="social"><span></span><span></span><span></span><span></span><span></span></div>
  <div class="footer-nav">Home | About | Blog | Fitness | Nutrition | Selfcare | Shop | Contact us</div>
  <div class="copyright">Copyright © 2018 Maren Crowley Active · All rights reserved.</div>
</footer>

</body>
</html>
```